Redesign of business card for Birchline Mechanical

We are looking for a new design for our business cards for Birchline Mechanical. We are a plumbing & HVAC construction company, operating on the West Coast of Canada and USA. Logo attached.
Industry/Entity Type
Construction - Plumbing & HVAC
Contact Information for Business Card
Name, address, phone numbers, email, website address
Look and feel
Each slider illustrates characteristics of the customer's brand and the style your logo design should communicate.

```html
<!DOCTYPE html>
<html lang="en">
<head>
<meta charset="utf-8">
<title>Birchline Mechanical – Business Card</title>
<link href="https://fonts.googleapis.com/css2?family=Poppins:wght@400;500;700&display=swap" rel="stylesheet">
<style>
  :root {
    --page: #ffffff;
    --card-dark: #0a0a0a;
    --card-dark-soft: #1a1a1a;
    --card-light: #e6e6e6;
    --ink: #0b0b0b;
    --rule: #4a2a2a;
    --white: #ffffff;
  }
  html, body {
    margin: 0;
    padding: 0;
    width: 1200px;
    height: 1000px;
    overflow: hidden;
    background: var(--page);
    font-family: "Poppins", Arial, sans-serif;
    color: var(--ink);
  }
  .canvas { position: relative; width: 1200px; height: 1000px; }

  /* Front card */
  .card-front {
    position: absolute; left: 201px; top: 25px;
    width: 797px; height: 455px;
    border-radius: 18px; overflow: hidden;
    background: var(--card-dark);
  }
  .brand-pattern {
    position: absolute; inset: 0;
    background: linear-gradient(135deg, var(--card-dark) 0%, var(--card-dark-soft) 50%, var(--card-dark) 100%);
  }
  .brand-tile {
    position: absolute; left: 531px; top: 229px;
    width: 174px; height: 161px;
    background: var(--white);
    display: flex; align-items: center; justify-content: center;
  }
  .brand-name {
    margin: 0; text-align: center;
    font-weight: 700; font-size: 21px; line-height: 1.15;
    color: var(--ink);
  }

  /* Back card */
  .card-back {
    position: absolute; left: 201px; top: 502px;
    width: 797px; height: 455px;
    border-radius: 18px; overflow: hidden;
    background: var(--card-light);
  }
  .fold-shade {
    position: absolute; left: 428px; top: 0; width: 90px; height: 100%;
    background: linear-gradient(90deg, rgba(0,0,0,0.06) 0%, rgba(0,0,0,0.16) 12%, rgba(0,0,0,0.05) 55%, rgba(0,0,0,0) 100%);
  }
  .contact {
    position: absolute; left: 0; top: 0; width: 423px;
    text-align: center;
  }
  .person-name {
    position: absolute; left: 0; right: 0; top: 74px;
    margin: 0; font-weight: 700; font-size: 31px; letter-spacing: 0.3px;
  }
  .person-role {
    position: absolute; left: 0; right: 0; top: 117px;
    margin: 0; font-weight: 500; font-size: 19px;
  }
  .icon-row {
    position: absolute; left: 76px; top: 172px; width: 271px; height: 24px;
  }
  .contact-line {
    position: absolute; left: 0; right: 0;
    margin: 0; font-weight: 500; font-size: 19px; line-height: 28px;
  }
  .phone { top: 219px; }
  .email { top: 260px; }
  .web { top: 301px; }
  .address { top: 345px; }
  .brand-back {
    position: absolute; left: 500px; top: 190px; width: 240px;
    text-align: center;
  }
</style>
</head>
<body>
<main class="canvas">

  <section class="card-front">
    <div class="brand-pattern" role="img" aria-label="Repeating faint brand pattern across dark card background"></div>
    <div class="brand-tile">
      <p class="brand-name">Birchline<br>Mechanical</p>
    </div>
  </section>

  <section class="card-back">
    <div class="fold-shade"></div>
    <div class="contact">
      <h1 class="person-name">Daniel Hartley</h1>
      <p class="person-role">Managing Director</p>

      <svg class="icon-row" viewBox="0 0 271 24" aria-hidden="true">
        <line x1="0" y1="12" x2="70" y2="12" stroke="var(--rule)" stroke-width="1.2"/>
        <line x1="201" y1="12" x2="271" y2="12" stroke="var(--rule)" stroke-width="1.2"/>
        <!-- phone -->
        <rect x="76" y="0" width="25" height="25" fill="var(--ink)"/>
        <path d="M81 11 q7.5 -6 15 0 l-1.5 2 h-2.5 l-0.5 -2 h-6 l-0.5 2 h-2.5 z M83 14 h11 v5 h-11 z" fill="var(--white)"/>
        <!-- mail -->
        <rect x="107" y="0" width="25" height="25" fill="var(--ink)"/>
        <rect x="111" y="7" width="17" height="11" fill="none" stroke="var(--white)" stroke-width="1.5"/>
        <path d="M111 7 l8.5 6 l8.5 -6" fill="none" stroke="var(--white)" stroke-width="1.5"/>
        <!-- globe -->
        <rect x="138" y="0" width="25" height="25" fill="var(--ink)"/>
        <circle cx="150.5" cy="12.5" r="7" fill="none" stroke="var(--white)" stroke-width="1.4"/>
        <ellipse cx="150.5" cy="12.5" rx="3" ry="7" fill="none" stroke="var(--white)" stroke-width="1.1"/>
        <line x1="143.5" y1="12.5" x2="157.5" y2="12.5" stroke="var(--white)" stroke-width="1.1"/>
        <!-- pin -->
        <rect x="169" y="0" width="25" height="25" fill="var(--ink)"/>
        <path d="M181.5 20 c-4 -5 -6 -7.5 -6 -10.5 a6 6 0 0 1 12 0 c0 3 -2 5.5 -6 10.5 z" fill="var(--white)"/>
        <circle cx="181.5" cy="9.5" r="2.2" fill="var(--ink)"/>
      </svg>

      <p class="contact-line phone">044-321 654 987</p>
      <p class="contact-line email">info@birchlinemech.com</p>
      <p class="contact-line web">www.birchlinemech.com</p>
      <p class="contact-line address">Apt. 218 40 Cedarwood Crossing,<br>North Fairhaven, ND 12345-6789</p>
    </div>

    <div class="brand-back">
      <p class="brand-name">Birchline<br>Mechanical</p>
    </div>
  </section>

</main>
</body>
</html>
```